Freelance business trainer needs a new business card

My business is called Tbrite. I provide training in the workplace on management, coaching and mentoring, and customer service topics for a variety of businesses, colleges and private training providers, and teach on management programs. I need a professional but eye catching business card. Business colours grey and orange. My name Linda Marchbank; Tel 07853 416207; email lmarchbank@tbrite.co.uk; website www.tbrite.co.uk.
Happy to have some sort of logo on front and details on back or all on one side
Target Market(s)
SME businesses and colleges - workshops i run are for adults in the workplace
Industry/Entity Type
Training
Look and feel

```html
<!DOCTYPE html>
<html lang="en">
<head>
<meta charset="utf-8">
<title>Tbrite business card</title>
<link rel="stylesheet" href="https://fonts.googleapis.com/css2?family=Montserrat:wght@400;700&display=swap">
<style>
  :root {
    --orange: #ec8a23;
    --orange-deep: #e07b17;
    --card-white: #f4f4f2;
    --ink: #1e1e1e;
    --ink-soft: #2d2d2d;
    --stage: #6e6e6e;
    --rule: #3a3a3a;
  }
  * { margin: 0; padding: 0; box-sizing: border-box; }
  html, body {
    width: 1200px; height: 1000px; overflow: hidden;
    background: var(--stage);
    font-family: "Montserrat", sans-serif;
  }
  .canvas {
    position: relative; width: 1200px; height: 1000px;
    display: flex; flex-direction: column; align-items: center; justify-content: center; gap: 60px;
  }
  .card {
    position: relative; width: 640px; height: 366px;
    box-shadow: 0 6px 18px rgba(0,0,0,.25);
    overflow: hidden;
  }

  /* Back side */
  .card--back {
    background: var(--orange);
    display: flex; align-items: center; justify-content: center;
  }
  .back-mark {
    width: 220px; height: 220px; border-radius: 50%;
    background: var(--card-white);
    display: flex; align-items: center; justify-content: center;
  }
  .back-mark__name {
    color: var(--orange); font-weight: 400; font-size: 50px; letter-spacing: 1px;
  }

  /* Front side */
  .card--front { background: var(--card-white); }
  .front-mark {
    position: absolute; left: 44px; top: 74px;
    width: 192px; height: 192px; border-radius: 50%;
    background: var(--orange);
    display: flex; align-items: center; justify-content: center;
  }
  .front-mark__name {
    color: #fff; font-weight: 400; font-size: 42px; letter-spacing: 1px;
  }
  .divider {
    position: absolute; left: 276px; top: 26px; height: 252px;
    border-left: 3px dotted var(--rule);
  }
  .details { position: absolute; left: 312px; top: 58px; }
  .details__name {
    font-size: 30px; color: var(--ink); font-weight: 400; margin-bottom: 54px;
  }
  .details__name strong { font-weight: 700; }
  .contact-list { list-style: none; }
  .contact-list li {
    display: flex; align-items: center; gap: 10px;
    font-size: 22px; color: var(--ink-soft); line-height: 32px;
  }
  .contact-icon { width: 18px; height: 18px; flex: none; }
  .footer-band {
    position: absolute; left: 0; right: 0; bottom: 0; height: 58px;
    background: var(--orange-deep);
  }
  .footer-band::before {
    content: ""; position: absolute; left: 0; right: 0; top: 12px;
    height: 2px; background: var(--card-white);
  }
</style>
</head>
<body>
<main class="canvas">
  <section class="card card--back" aria-label="Card back">
    <div class="back-mark"><span class="back-mark__name">Tbrite</span></div>
  </section>

  <section class="card card--front" aria-label="Card front">
    <div class="front-mark"><span class="front-mark__name">Tbrite</span></div>
    <div class="divider"></div>
    <div class="details">
      <h1 class="details__name"><strong>Linda</strong> Marchbank</h1>
      <ul class="contact-list">
        <li>
          <svg class="contact-icon" viewBox="0 0 18 18" aria-hidden="true">
            <circle cx="9" cy="9" r="9" fill="var(--orange)"/>
            <path d="M6 4.5l1.6 2.2-1 1.1a6 6 0 0 0 3.6 3.6l1.1-1 2.2 1.6-.9 1.5c-3.8.2-7.9-3.9-7.7-7.7z" fill="#fff"/>
          </svg>
          07853 416207
        </li>
        <li>
          <svg class="contact-icon" viewBox="0 0 18 18" aria-hidden="true">
            <circle cx="9" cy="9" r="9" fill="var(--orange)"/>
            <rect x="4.5" y="6" width="9" height="6.5" fill="#fff"/>
            <path d="M4.5 6l4.5 3.6L13.5 6" fill="none" stroke="var(--orange)" stroke-width="1"/>
          </svg>
          lmarchbank@tbrite.co.uk
        </li>
        <li>
          <svg class="contact-icon" viewBox="0 0 18 18" aria-hidden="true">
            <circle cx="9" cy="9" r="9" fill="var(--orange)"/>
            <text x="9" y="11" text-anchor="middle" font-size="5" font-family="Montserrat, sans-serif" font-weight="700" fill="#fff">www</text>
          </svg>
          www.tbrite.co.uk.
        </li>
      </ul>
    </div>
    <div class="footer-band"></div>
  </section>
</main>
</body>
</html>
```